Create PP presentation that explains the one on one on camera video series that features the world's top real estate developers, builders, investors, banks, lawyers, academics and policy makers. It will be a hard hitting frank discussion about the real issues that the COMMERCIAL (not residential) real estate industry is dealing with. The marketing should be news network looking with high tech look and feel and show that it is provides serious and useful financial news content. We are a commercial real estate firm that has established a media arm to provide REAL TIME information regarding the real estate market place. Examples of look and feel should be KVRTN or Halvorsen TV. Two pp have been attached should be able to tell that they are from the same company but encourage to take your own approach. A full pp presentation has been included title Summit Dialogues - make it your own. You do not have to use the same images that were provided, these are just guidelines as to what we want to communicate. The layout can be changed - we are using bullet points but if you have a better way to present the information, please do so.

Summit

```html
<!DOCTYPE html>
<html lang="en">
<head>
<meta charset="utf-8">
<title>Interviews with Real Estate Icons</title>
<link href="https://fonts.googleapis.com/css2?family=Roboto+Condensed:wght@400;700&display=swap" rel="stylesheet">
<style>
  :root {
    --ink: #333333;
    --accent-blue: #1d3fc4;
    --header-top: #ffffff;
    --header-bottom: #cfe9f7;
    --sky-light: #9fc8dc;
    --glass-mid: #3f8ea3;
    --glass-deep: #1f5b72;
    --panel: #ffffff;
    --footer: #4a4a4a;
    --footer-text: #ffffff;
    --ring: #ffffff;
  }
  * { margin: 0; padding: 0; box-sizing: border-box; }
  html, body { width: 1200px; height: 900px; overflow: hidden; }
  body { font-family: "Roboto Condensed", "Arial Narrow", sans-serif; background: #ffffff; }

  .slide { position: relative; width: 1200px; height: 900px; overflow: hidden; }

  .slide-header {
    position: absolute; left: 0; top: 0; width: 1200px; height: 104px;
    background: linear-gradient(180deg, var(--header-top) 0%, #eef7fc 45%, var(--header-bottom) 100%);
    border-bottom: 3px solid #ffffff;
    display: flex; align-items: center; padding-left: 36px;
  }
  .slide-title { font-size: 42px; font-weight: 700; color: var(--ink); letter-spacing: -0.3px; }
  .slide-title .highlight { color: var(--accent-blue); }

  .backdrop {
    position: absolute; left: 0; top: 107px; width: 1200px; height: 725px;
    background:
      linear-gradient(90deg, rgba(160,200,220,0.55) 0%, rgba(60,140,165,0.15) 40%, rgba(30,90,115,0.2) 65%, rgba(150,190,210,0.5) 100%),
      linear-gradient(180deg, var(--sky-light) 0%, var(--glass-mid) 45%, var(--glass-deep) 100%);
  }

  .content-panel {
    position: absolute; left: 40px; top: 152px; width: 500px; height: 571px;
    background: var(--panel); padding: 36px 0 0 22px;
  }
  .series-heading { font-size: 27px; font-weight: 700; color: var(--ink); line-height: 1; margin-bottom: 33px; }
  .series-heading.second { margin-top: 0; margin-bottom: 31px; }
  .series-list { list-style: none; margin: 0 0 0 24px; }
  .series-list li {
    font-size: 26px; color: var(--ink); line-height: 1; height: 58.5px;
    display: flex; align-items: flex-start;
  }
  .series-list li svg { width: 14px; height: 20px; margin: 3px 12px 0 0; flex: none; }

  .photo-bubble {
    position: absolute; border-radius: 50%; border: 4px solid var(--ring);
    box-shadow: 0 2px 8px rgba(0,0,0,0.35);
  }
  .bubble-hardhats { left: 828px; top: 207px; width: 144px; height: 144px; background: radial-gradient(circle at 40% 40%, #e8c98a, #7d9bb0); }
  .bubble-world-map { left: 706px; top: 311px; width: 144px; height: 144px; background: radial-gradient(circle at 45% 45%, #3fb3d6, #0d5f8a); }
  .bubble-glass-tower { left: 986px; top: 289px; width: 144px; height: 144px; background: radial-gradient(circle at 40% 40%, #d8dde0, #7a6350); }
  .bubble-gavel { left: 846px; top: 373px; width: 144px; height: 144px; background: radial-gradient(circle at 50% 50%, #c98a3c, #4a2a12); }
  .bubble-city-traffic { left: 717px; top: 474px; width: 136px; height: 136px; background: radial-gradient(circle at 50% 50%, #c9b77a, #4d5a64); }
  .bubble-bank-facade { left: 1012px; top: 450px; width: 144px; height: 144px; background: radial-gradient(circle at 50% 50%, #a88a6a, #4a3a2c); }
  .bubble-construction { left: 876px; top: 526px; width: 144px; height: 144px; background: radial-gradient(circle at 50% 35%, #d9eaf5, #7f97a6); }

  .slide-footer {
    position: absolute; left: 0; top: 832px; width: 1200px; height: 68px;
    background: var(--footer);
  }
  .copyright { position: absolute; left: 21px; top: 23px; font-size: 19px; color: var(--footer-text); }
  .brand-box {
    position: absolute; left: 915px; top: 829px; width: 285px; height: 71px;
    background: #ffffff; display: flex; align-items: center; justify-content: center;
  }
  .brand-name { font-size: 34px; font-weight: 400; color: var(--ink); letter-spacing: 0.5px; }
</style>
</head>
<body>
<div class="slide">
  <div class="backdrop" role="img" aria-label="Photo of a curved blue glass skyscraper among city towers"></div>

  <header class="slide-header">
    <h1 class="slide-title">Interviews with <span class="highlight">Real Estate Icons</span></h1>
  </header>

  <section class="content-panel">
    <h2 class="series-heading">Five Market Segment Series 2014 / 15</h2>
    <ul class="series-list">
      <li><svg viewBox="0 0 14 20"><path d="M2 2 L11 10 L2 18" fill="none" stroke="#333" stroke-width="3.5"/></svg>Developers and Builders</li>
      <li><svg viewBox="0 0 14 20"><path d="M2 2 L11 10 L2 18" fill="none" stroke="#333" stroke-width="3.5"/></svg>Financial Service Providers</li>
      <li><svg viewBox="0 0 14 20"><path d="M2 2 L11 10 L2 18" fill="none" stroke="#333" stroke-width="3.5"/></svg>Legal Practitioners and Scholars</li>
      <li><svg viewBox="0 0 14 20"><path d="M2 2 L11 10 L2 18" fill="none" stroke="#333" stroke-width="3.5"/></svg>Brokerage and Technology</li>
      <li><svg viewBox="0 0 14 20"><path d="M2 2 L11 10 L2 18" fill="none" stroke="#333" stroke-width="3.5"/></svg>Public Sector</li>
    </ul>
    <h2 class="series-heading second">Twenty Four Annual Interviews</h2>
    <ul class="series-list">
      <li><svg viewBox="0 0 14 20"><path d="M2 2 L11 10 L2 18" fill="none" stroke="#333" stroke-width="3.5"/></svg>Produced bi-weekly</li>
      <li><svg viewBox="0 0 14 20"><path d="M2 2 L11 10 L2 18" fill="none" stroke="#333" stroke-width="3.5"/></svg>Content adjusted to market events</li>
    </ul>
  </section>

  <div class="photo-bubble bubble-hardhats" role="img" aria-label="Photo of construction managers in hard hats"></div>
  <div class="photo-bubble bubble-world-map" role="img" aria-label="Digital world map graphic in blue"></div>
  <div class="photo-bubble bubble-glass-tower" role="img" aria-label="Photo of a glass office tower facade"></div>
  <div class="photo-bubble bubble-gavel" role="img" aria-label="Photo of a judge's gavel and scales"></div>
  <div class="photo-bubble bubble-city-traffic" role="img" aria-label="Photo of busy city street with taxis"></div>
  <div class="photo-bubble bubble-bank-facade" role="img" aria-label="Photo of a classic bank building facade"></div>
  <div class="photo-bubble bubble-construction" role="img" aria-label="Photo of high-rise towers under construction with crane"></div>

  <footer class="slide-footer">
    <p class="copyright">Copyright text here</p>
  </footer>
  <div class="brand-box"><span class="brand-name">Harborline</span></div>
</div>
</body>
</html>
```